Website for Corvalind Capital, my new firm that raises money from investors to buy, build, own an...

Corvalind Capital needs a website! We are a new company with very experienced people, who invest in, own and build hotel properties, as well as apartments and other commercial real estate. We seek investors for our projects, and we provide safe, secure returns on their investment in our projects. Our new logo is designed to exhibit strength, class and security, and would like our website to continue on this theme. Our name, Corvalind, is a word-play on a Greek word “aristeia”, which means “excellence” and “a warriors finest moment of glory in war”. If you are in business, you realize that much of it is like war, with strategy and moves and opponents and competitors, and ever-changing economic conditions and threats that make business very much like war. We like to think that we are good at business (war), and so have named our company “Corvalind”, using the founders last name and the word “aristeia” combined. Another definition of "aristeia" is "performing at the peak of one's potential after a long struggle"...again, much like business in real life! The website design should exhibit financial security, smart moves, and positive growth towards a bright future.

Target Market(s)

The target market is smart and wealthy investors, with others such as brokers, cities and government agencies, lenders, sellers, partners, etc also looking at it.

Industry/Entity Type

Investment

Number of Pages Required

5+ page

Font styles to use
Sans Serif

Colors
fec214

Requirements
Must have
• Our website should have a landing page, a "about" or bio page, a projects page and a contact us page. Our new logo uses the colors black and gold, so this should be factored in to our site. The site should be simple, yet impactful and impressive. I have actually two logos, which can be mixed and interchanged in a complimentary way, each with their own unique look.
Nice to have
• I have uploaded a couple screenshots of a website i like, and the simplicity I mention.
Should not have
• The site should not be flashy or complicated or complex or "busy"

```html
<!DOCTYPE html>
<html lang="en">
<head>
<meta charset="utf-8">
<title>Corvalind Capital</title>
<link rel="stylesheet" href="https://fonts.googleapis.com/css2?family=Poppins:wght@400;500;600;700&family=Open+Sans:wght@400;600&display=swap">
<style>
  :root {
    --gold: #fec214;
    --ink: #111111;
    --dark: #1b1b1b;
    --charcoal: #262626;
    --white: #ffffff;
    --text: #333333;
    --muted: #9a9a9a;
    --hero-a: #dfe6ee;
    --hero-b: #9fb1c4;
  }
  * { margin: 0; padding: 0; box-sizing: border-box; }
  html, body { width: 1200px; height: 3196px; overflow: hidden; }
  body { position: relative; background: var(--white); font-family: "Open Sans", sans-serif; color: var(--text); }
  .abs { position: absolute; }
  .heading { font-family: "Poppins", sans-serif; }

  /* Header */
  .site-header { position: absolute; top: 0; left: 0; width: 1200px; height: 120px; background: var(--white); }
  .brand { position: absolute; left: 100px; top: 22px; display: flex; align-items: center; gap: 12px; }
  .brand-mark { width: 34px; height: 34px; background: var(--gold); }
  .brand-name { font-family: "Poppins", sans-serif; font-weight: 600; font-size: 17px; line-height: 1.1; color: var(--ink); letter-spacing: 1px; }
  .social-top { position: absolute; left: 944px; top: 8px; display: flex; gap: 8px; }
  .social-top span { width: 30px; height: 30px; background: var(--ink); }
  .main-nav { position: absolute; left: 580px; top: 62px; display: flex; gap: 40px; font-family: "Poppins", sans-serif; font-size: 14px; font-weight: 500; color: var(--ink); }
  .nav-search { position: absolute; left: 1080px; top: 62px; }

  /* Hero */
  .hero { position: absolute; top: 120px; left: 0; width: 1200px; height: 600px; background: linear-gradient(180deg, var(--hero-a), var(--hero-b)); }
  .hero-title { position: absolute; top: 160px; width: 100%; text-align: center; font-family: "Poppins", sans-serif; font-weight: 700; font-size: 64px; letter-spacing: 3px; color: var(--ink); }
  .hero-lead { position: absolute; top: 258px; left: 320px; width: 560px; text-align: center; font-family: "Poppins", sans-serif; font-size: 21px; line-height: 1.5; color: var(--ink); }
  .btn { display: inline-block; background: var(--gold); color: var(--white); font-family: "Poppins", sans-serif; font-size: 14px; font-weight: 500; text-transform: uppercase; text-align: center; }
  .hero-btn { position: absolute; top: 372px; left: 488px; width: 224px; height: 48px; line-height: 48px; }
  .hero-arrow { position: absolute; top: 540px; left: 570px; }

  /* Quote slider */
  .statement { position: absolute; top: 720px; left: 0; width: 1200px; height: 520px; background: linear-gradient(180deg, #57606a, #3c4249 60%, #2d3136); }
  .statement-text { position: absolute; top: 90px; left: 220px; width: 760px; text-align: center; font-family: "Poppins", sans-serif; font-size: 25px; line-height: 1.55; color: var(--white); }
  .statement-rule { position: absolute; top: 300px; left: 555px; width: 90px; height: 3px; background: var(--gold); }
  .statement-name { position: absolute; top: 338px; width: 100%; text-align: center; font-family: "Poppins", sans-serif; font-size: 18px; font-weight: 500; letter-spacing: 1px; color: var(--white); }
  .dots { position: absolute; display: flex; gap: 8px; }
  .dots span { width: 9px; height: 9px; border-radius: 50%; background: rgba(255,255,255,0.6); }
  .dots span.on { background: var(--white); }

  /* Services */
  .services { position: absolute; top: 1240px; left: 0; width: 1200px; height: 440px; background: var(--dark); }
  .section-title { position: absolute; width: 100%; text-align: center; font-family: "Poppins", sans-serif; font-weight: 600; font-size: 46px; }
  .section-rule { position: absolute; left: 560px; width: 80px; height: 3px; background: var(--gold); }
  .section-sub { position: absolute; width: 100%; text-align: center; font-size: 13px; }
  .service-card { position: absolute; top: 1504px; width: 324px; height: 376px; background: var(--charcoal); }
  .service-card .photo { width: 100%; height: 296px; }
  .service-card .caption { height: 80px; line-height: 80px; text-align: center; font-family: "Poppins", sans-serif; font-size: 14px; font-weight: 500; color: var(--white); background: var(--ink); }

  /* About */
  .about-text { position: absolute; top: 2060px; left: 230px; width: 740px; text-align: center; font-size: 13.5px; line-height: 2; color: var(--text); }
  .about-btn { position: absolute; top: 2216px; left: 520px; width: 160px; height: 46px; line-height: 46px; }

  /* Investment */
  .investment { position: absolute; top: 2368px; left: 0; width: 1200px; height: 512px; background: linear-gradient(135deg, #4e5b68, #2f3842 55%, #3e4854); }
  .investment-title { position: absolute; top: 86px; left: 170px; font-family: "Poppins", sans-serif; font-size: 40px; font-weight: 500; color: var(--white); }
  .investment-rule { position: absolute; top: 150px; left: 170px; width: 80px; height: 3px; background: var(--gold); }
  .investment-quote { position: absolute; top: 180px; left: 330px; width: 570px; text-align: center; font-family: "Poppins", sans-serif; font-size: 21px; line-height: 1.6; color: var(--white); }

  /* Footer */
  .site-footer { position: absolute; top: 2880px; left: 0; width: 1200px; height: 316px; background: var(--ink); color: #cfcfcf; }
  .footer-col { position: absolute; top: 46px; font-size: 13px; line-height: 1.75; }
  .footer-col h4 { font-family: "Poppins", sans-serif; font-weight: 500; font-size: 18px; color: var(--white); margin-bottom: 10px; }
  .footer-social { display: flex; gap: 12px; }
  .footer-social span { width: 16px; height: 16px; border-radius: 50%; background: #cfcfcf; }
  .contact-line { display: flex; align-items: center; gap: 8px; }
  .news-input { width: 270px; height: 40px; border: 1px solid #555; background: var(--ink); font-size: 12px; line-height: 38px; padding-left: 12px; color: var(--muted); }
  .news-btn { width: 270px; height: 40px; line-height: 40px; margin-top: 12px; }
  .copyright { position: absolute; top: 270px; left: 100px; font-size: 12px; color: var(--muted); }
</style>
</head>
<body>

<header class="site-header">
  <div class="brand">
    <div class="brand-mark"></div>
    <div class="brand-name">CORVALIND<br>CAPITAL</div>
  </div>
  <div class="social-top"><span></span><span></span><span></span><span></span><span></span></div>
  <nav class="main-nav"><span>HOME</span><span>ABOUT US</span><span>PROJECT</span><span>CONTACT US</span></nav>
  <svg class="nav-search" width="18" height="18" viewBox="0 0 18 18"><circle cx="7.5" cy="7.5" r="5.5" fill="none" stroke="#111" stroke-width="2"/><line x1="11.5" y1="11.5" x2="16.5" y2="16.5" stroke="#111" stroke-width="2"/></svg>
</header>

<section class="hero" role="img" aria-label="Photo of a modern glass skyscraper city skyline in pale blue light">
  <h1 class="hero-title">CORVALIND CAPITAL</h1>
  <p class="hero-lead">Experienced people, who invest in, own and build hotel properties, as well as apartments and other commercial real estate.</p>
  <span class="btn hero-btn">Contact us now</span>
  <svg class="hero-arrow" width="60" height="34" viewBox="0 0 60 34"><polyline points="4,4 30,28 56,4" fill="none" stroke="#111" stroke-width="4"/></svg>
</section>

<section class="statement" role="img" aria-label="Photo of a paved city plaza with trees and buildings under a dark overlay">
  <p class="statement-text">Lorem ipsum dolor sit amet, tetuering elit, sed do eiusmod tdunt ut labore et dolore magna aliqua. Ut enim ad minim veniam, quis nostrud exercitation ullamco laboris nisi ut liquip &nbsp;ex ea modo consequat.</p>
  <div class="statement-rule"></div>
  <div class="statement-name">CORVALIND CAPITAL</div>
  <div class="dots" style="top:420px;left:566px;"><span class="on"></span><span></span><span></span><span></span></div>
</section>

<section class="services">
  <h2 class="section-title" style="top:90px;color:var(--white);">WHAT WE DO ?</h2>
  <div class="section-rule" style="top:160px;"></div>
  <p class="section-sub" style="top:188px;color:#d0d0d0;">Lorem ipsum dolor sit amet, consectetur adipiscing elit, sed do eiusmod tempor incididunt.</p>
</section>

<article class="service-card" style="left:100px;">
  <div class="photo" role="img" aria-label="Photo of a desk with papers, laptop and a potted plant seen from above" style="background:linear-gradient(135deg,#6d5a48,#c8b9a4 55%,#3a5f86);"></div>
  <div class="caption">SED UT PERSPICIATIS UNDE</div>
</article>
<article class="service-card" style="left:438px;">
  <div class="photo" role="img" aria-label="Photo of a business meeting with hands over documents" style="background:linear-gradient(135deg,#2c2a28,#8a7c6c 55%,#d8d2ca);"></div>
  <div class="caption">SED UT PERSPICIATIS UNDE</div>
</article>
<article class="service-card" style="left:776px;">
  <div class="photo" role="img" aria-label="Photo of tall glass office towers against a blue sky" style="background:linear-gradient(180deg,#1f3f6e,#4d78a8 50%,#22344c);"></div>
  <div class="caption">SED UT PERSPICIATIS UNDE</div>
</article>

<section class="about">
  <h2 class="section-title" style="top:1960px;color:var(--ink);">ABOUT US</h2>
  <div class="section-rule" style="top:2030px;"></div>
  <p class="about-text">Lorem ipsum dolor sit amet, consectetur adipiscing elit, sed do eiusmod tempor incididunt ut labore et dolore magna aliqua. Ut enim ad minim veniam, quis nostrud exercitation ullamco laboris nisi ut aliquip ex ea commodo consequat. Duis aute irure dolor in reprehenderit in voluptate velit esse cillum dolore eu fugiat nulla pariatur.</p>
  <span class="btn about-btn">Learn more</span>
</section>

<section class="investment" role="img" aria-label="Photo of a modern steel and glass building structure under a dark overlay">
  <h2 class="investment-title">AN INVESTMENT WE'VE MADE</h2>
  <div class="investment-rule"></div>
  <p class="investment-quote">"Sed ut perspiciatis unde omnis iste natus error sit voluptatem accusantium, totam rem aperiam, eaque ipsa quae ab illo inventore veritatis et quasi architecto beatae vitae dicta sunt explicabo.</p>
  <div class="dots" style="top:362px;left:572px;"><span></span><span class="on" style="background:var(--gold);"></span><span></span></div>
</section>

<footer class="site-footer">
  <div class="footer-col" style="left:100px;">
    <h4>Main menu</h4>
    Home<br>About Us<br>Projects<br>Contact Us
  </div>
  <div class="footer-col" style="left:322px;">
    <h4>Stay In Touch</h4>
    <div class="footer-social"><span></span><span></span><span></span><span></span></div>
  </div>
  <div class="footer-col" style="left:564px;">
    <h4>Contact Us</h4>
    <div>1480 Harbor Ridge Ave, Suite 200</div>
    <div class="contact-line"><svg width="12" height="12" viewBox="0 0 12 12"><path d="M2 1h3l1 3-2 1a7 7 0 0 0 3 3l1-2 3 1v3a1 1 0 0 1-1 1A10 10 0 0 1 1 2a1 1 0 0 1 1-1z" fill="#cfcfcf"/></svg>+1 555 014 2290</div>
    <div class="contact-line"><svg width="12" height="10" viewBox="0 0 12 10"><rect x="0.5" y="0.5" width="11" height="9" fill="none" stroke="#cfcfcf"/><polyline points="0.5,0.5 6,5 11.5,0.5" fill="none" stroke="#cfcfcf"/></svg>info@corvalindcapital.com</div>
  </div>
  <div class="footer-col" style="left:830px;">
    <h4>News &amp; updates</h4>
    <div class="news-input">Enter Your email address</div>
    <div class="btn news-btn">Sign up</div>
  </div>
  <p class="copyright">© Copyright 2018 Corvalind Capital. All Rights Reserved.</p>
</footer>

</body>
</html>
```